Flyer Design Project

Something bold, something creative, something colorful. Will have 3 full time employees passing these out to business owners locally as well as national conventions.
Need something that will grab attention and remain a reminder, before they end up hitting the trash can...
Site can be found at www.QuillOrbitPress.example
A few different logo formats are attached.
2 sizes would be nice. 8.5" x 11" and 4"x6 (they can look the same)
No specifics on graphics, colors or info. Stay somewhat consistent with the website. I basically just want people to know we are here and we are definitely the cheapest print prices in the nation.
Target Market(s)
Anyone that needs print work done.
Industry/Entity Type
Business
Look and feel

```html
<!DOCTYPE html>
<html lang="en">
<head>
<meta charset="utf-8">
<title>QuillOrbit Flyer</title>
<link rel="stylesheet" href="https://fonts.googleapis.com/css2?family=League+Spartan:wght@800&family=Questrial&family=Arimo:ital,wght@0,400;1,400;1,700&display=swap">
<style>
  :root {
    --frame-orange: #ea7b22;
    --lime: #a3cd4a;
    --ink: #0b0b0b;
    --paper: #ffffff;
    --teal: #4cb7cc;
    --yellow: #ffff1a;
  }
  html, body {
    margin: 0;
    padding: 0;
    width: 851px;
    height: 1200px;
    overflow: hidden;
    background: var(--paper);
  }
  .board {
    position: relative;
    width: 851px;
    height: 1200px;
  }
  .board-frame {
    position: absolute;
    left: 4px; top: 4px;
    width: 829px; height: 1178px;
    border: 7px solid var(--frame-orange);
    border-radius: 62px;
  }
  .flyer {
    position: absolute;
    left: 66px; top: 52px;
    width: 722px; height: 1023px;
    background: var(--ink);
  }
  .flyer-topband {
    position: absolute;
    left: 0; top: 0;
    width: 100%; height: 36px;
    background: var(--lime);
  }
  .brand {
    position: absolute;
    left: 80px; top: 85px;
    display: flex;
    align-items: center;
    gap: 34px;
  }
  .brand-mark {
    width: 130px; height: 130px;
    border-radius: 50%;
    background: var(--lime);
  }
  .brand-text {
    display: flex;
    flex-direction: column;
  }
  .brand-name {
    font-family: "Questrial", sans-serif;
    font-size: 74px;
    line-height: 1;
    color: var(--lime);
    letter-spacing: -1px;
  }
  .brand-tagline {
    font-family: "Questrial", sans-serif;
    font-size: 25px;
    color: var(--teal);
    margin-top: 6px;
    margin-left: 10px;
  }
  .panel {
    position: absolute;
    left: 20px; top: 226px;
    width: 682px; height: 777px;
    background: var(--lime);
  }
  .headline {
    position: absolute;
    left: 0; top: 28px;
    width: 100%;
    margin: 0;
    text-align: center;
    font-family: "League Spartan", sans-serif;
    font-weight: 800;
    font-size: 120px;
    line-height: 144px;
    color: var(--ink);
    text-shadow: 0 0 6px #fff, 0 0 10px #fff, 0 0 14px #fff;
  }
  .headline span { display: block; }
  .guarantee {
    position: absolute;
    left: 10px; top: 605px;
    width: 682px;
    text-align: center;
    font-family: "Arimo", sans-serif;
    font-style: italic;
    font-weight: 700;
    font-size: 45px;
    color: var(--yellow);
    transform: rotate(-5deg);
  }
  .contact {
    position: absolute;
    left: 0; top: 736px;
    width: 100%;
    text-align: center;
    font-family: "Arimo", sans-serif;
    font-size: 20px;
    color: var(--ink);
  }
  .spec-label {
    position: absolute;
    left: 100px; top: 1117px;
    font-family: "Arimo", sans-serif;
    font-style: italic;
    font-size: 17px;
    color: #222;
  }
  .spec-rule {
    position: absolute;
    left: 98px; top: 1140px;
    width: 594px; height: 4px;
    background: var(--frame-orange);
  }
</style>
</head>
<body>
<div class="board">
  <div class="board-frame"></div>

  <div class="flyer">
    <div class="flyer-topband"></div>

    <div class="brand">
      <div class="brand-mark"></div>
      <div class="brand-text">
        <div class="brand-name">QuillOrbit</div>
        <div class="brand-tagline">Discount Print and Promo</div>
      </div>
    </div>

    <div class="panel">
      <h1 class="headline">
        <span>NOBODY</span>
        <span>BEATS</span>
        <span>OUR PRINT</span>
        <span>PRICES</span>
      </h1>
      <div class="guarantee">100% Customer Guarantee</div>
      <div class="contact">Telephone: 555.010.2468 - U.S. Fax: 555.010.3579</div>
    </div>
  </div>

  <div class="spec-label">A4 Flyer 8.5" x 11"</div>
  <div class="spec-rule"></div>
</div>
</body>
</html>
```